Business Stationery Design

I would like to get some stationery designed for my company. The stationery should include a letterhead, envelope, and business card. We are a technology consulting company specializing in Healthcare IT, and Education management systems. The colors of the stationery should match the logo. The logo is uploaded.

Target Market(s)

Hospitals, Clinics. Doctors offices. Private Schools.

Industry/Entity Type

Business

```html
<!DOCTYPE html>
<html lang="en">
<head>
<meta charset="utf-8">
<title>Clearpath Advisory Group – Stationery</title>
<link href="https://fonts.googleapis.com/css2?family=Source+Sans+3:wght@400;600&display=swap" rel="stylesheet">
<style>
  :root{
    --green:#77bd32;
    --yellow:#f5b300;
    --ink:#333333;
    --paper:#ffffff;
    --backdrop:#dcdcdc;
  }
  *{box-sizing:border-box;margin:0;padding:0}
  html,body{width:1200px;height:722px;overflow:hidden}
  body{background:var(--backdrop);font-family:"Source Sans 3",sans-serif;color:var(--ink);position:relative}
  .sheet{position:absolute;background:var(--paper);overflow:hidden}
  .wave{position:absolute;left:0;bottom:0;width:100%}
  .brand{color:var(--green);font-weight:600;line-height:1.05;position:absolute}
  .brand small{display:block;font-size:.45em}
  .contact{position:absolute;font-size:7px;line-height:8.5px}
  .contact .row{display:flex;align-items:center;gap:3px}
  .contact svg{width:6px;height:6px;fill:var(--green)}
  .web{position:absolute;color:#fff;font-size:8px}

  /* letterhead */
  .letterhead{left:230px;top:76px;width:385px;height:541px}
  .letterhead .brand{left:42px;top:74px;font-size:18px}
  .letterhead .contact{left:282px;top:24px}
  .letterhead .address{position:absolute;left:282px;top:88px;font-size:7px;line-height:8px}
  .letter{position:absolute;left:37px;top:124px;width:315px;font-size:7.2px;line-height:12px;text-align:justify}
  .letter p{margin-bottom:12px}
  .letter .salutation{margin-bottom:10px}
  .signature{position:absolute;left:37px;top:396px;width:115px;height:36px;background:linear-gradient(90deg,#e8e8e8,#f4f4f4)}
  .role{position:absolute;left:37px;top:442px;font-size:8px}
  .letterhead .web{right:36px;bottom:4px}

  /* business card */
  .card-front{left:653px;top:99px;width:189px;height:108px}
  .card-front .brand{right:12px;top:38px;font-size:10px;text-align:right}
  .card-front .person{position:absolute;left:13px;top:61px;font-size:5px}
  .card-front .person b{color:var(--green);font-weight:600;letter-spacing:.3px}
  .card-front .rule{position:absolute;left:13px;right:12px;top:70px;border-top:.6px solid var(--green)}
  .card-front .contact{left:13px;top:76px;font-size:5px;line-height:6.5px}
  .card-front .contact svg{width:4px;height:4px}
  .card-front .address{position:absolute;right:12px;top:82px;font-size:5px;line-height:6px}
  .card-front .web{right:14px;bottom:1px;font-size:5.5px}
  .card-back{left:850px;top:99px;width:189px;height:108px;background:var(--green)}
  .card-back .brand{color:#fff;left:0;right:0;top:38px;text-align:center;font-size:15px}

  /* envelope */
  .envelope-back{left:653px;top:224px;width:386px;height:181px;background:transparent}
  .envelope-back .body{position:absolute;inset:0;background:var(--paper)}
  .envelope-back svg{position:absolute;left:0;top:0}
  .envelope-back .brand{color:#fff;left:0;right:0;top:24px;text-align:center;font-size:10px}
  .envelope-front{left:653px;top:433px;width:386px;height:184px}
  .envelope-front .brand{left:26px;top:50px;font-size:14px}
  .envelope-front .address{position:absolute;left:21px;top:77px;font-size:6.5px;line-height:7.5px}
</style>
</head>
<body>

<section class="sheet letterhead">
  <div class="brand">Clearpath<small>Advisory Group</small></div>
  <div class="contact">
    <div class="row"><svg viewBox="0 0 10 10"><path d="M2 1h2l1 2.5-1.3 1a6 6 0 0 0 2.8 2.8l1-1.3L10 7v2a1 1 0 0 1-1 1A9 9 0 0 1 0 2a1 1 0 0 1 1-1z"/></svg>800.555.0142</div>
    <div class="row"><svg viewBox="0 0 10 10"><rect x="1" y="1" width="8" height="8" rx="1"/></svg>800.555.0178</div>
    <div class="row"><svg viewBox="0 0 10 10"><path d="M0 2h10v6H0z"/></svg>hello@clearpath.co</div>
  </div>
  <div class="address">4200 Linden Ave Suite 210,<br>Springfield USA 62704</div>
  <div class="letter">
    <p class="salutation">Dear Client</p>
    <p>Lorem ipsum dolor sit amet, consectetur adipiscing elit. Pellentesque semper purus ornare dolor eleifend aliquam. Integer molestie gravida sem a porttitor. Quisque pulvinar tellus ut ipsum molestie ultricies id non turpis. Phasellus feugiat ornare feugiat. Integer nec velit eu justo laoreet condimentum. Aenean non commodo quam. Phasellus lacinia aliquet turpis. Praesent non elit nec ante porta cursus. Morbi et augue enim, nec ultrices augue. Etiam tempus arcu laoreet metus tristique ultrices.</p>
    <p>Curabitur nec venenatis risus. Integer nec nisi sit amet leo mattis aliquam. Vivamus vulputate tellus quis purus lobortis rutrum. Aenean nec ipsum ut mauris faucibus facilisis vel porttitor neque. Morbi molestie magna id neque scelerisque ut iaculis justo porttitor. Sed est ligula, semper at cursus ac, porttitor ac ipsum. Maecenas pulvinar euismod tempor. Pellentesque habitant morbi tristique senectus et netus et malesuada fames ac turpis egestas. Integer nec velit turpis. Aliquam adipiscing massa sed ipsum commodo id ullamcorper leo volutpat. Sed vitae tellus dui.</p>
    <p>Maecenas vel neque ante, id faucibus ipsum. Suspendisse non neque quis nunc rhoncus bibendum. Fusce sit amet quam quis libero facilisis ultrices. Donec dignissim lorem vel sem sodales mollis. Duis nec sem lorem, at tristique nibh. In rutrum fermentum lectus, nec dictum leo tincidunt in. Nam metus odio, molestie a tempor a, laoreet placerat dui. Fusce sit amet nisi at elit bibendum imperdiet. Sed fringilla nisi non nunc facilisis in ullamcorper justo suscipit. Fusce fermentum tincidunt sagittis.</p>
  </div>
  <div class="signature" role="img" aria-label="Handwritten signature of the managing director"></div>
  <div class="role">Managing Director</div>
  <svg class="wave" viewBox="0 0 385 30" width="385" height="30" preserveAspectRatio="none">
    <path d="M30 30 Q170 3 360 2 L300 5 Q150 10 60 30Z" fill="var(--yellow)"/>
    <path d="M55 30 Q200 6 385 7 L385 30Z" fill="var(--green)"/>
  </svg>
  <div class="web">www.clearpath.co</div>
</section>

<section class="sheet card-front">
  <div class="brand">Clearpath<small>Advisory Group</small></div>
  <div class="person"><b>EMPLOYEE NAME</b><br>Title</div>
  <div class="rule"></div>
  <div class="contact">
    <div class="row"><svg viewBox="0 0 10 10"><path d="M2 1h2l1 2.5-1.3 1a6 6 0 0 0 2.8 2.8l1-1.3L10 7v2a1 1 0 0 1-1 1A9 9 0 0 1 0 2a1 1 0 0 1 1-1z"/></svg>800.555.0142</div>
    <div class="row"><svg viewBox="0 0 10 10"><rect x="1" y="1" width="8" height="8" rx="1"/></svg>800.555.0178</div>
    <div class="row"><svg viewBox="0 0 10 10"><path d="M0 2h10v6H0z"/></svg>hello@clearpath.co</div>
  </div>
  <div class="address">4200 Linden Ave Suite 210,<br>Springfield USA 62704</div>
  <svg class="wave" viewBox="0 0 189 14" width="189" height="14" preserveAspectRatio="none">
    <path d="M10 14 Q80 2 175 1 L150 3 Q70 6 25 14Z" fill="var(--yellow)"/>
    <path d="M25 14 Q100 3 189 3 L189 14Z" fill="var(--green)"/>
  </svg>
  <div class="web">www.clearpath.co</div>
</section>

<section class="sheet card-back">
  <div class="brand">Clearpath<small>Advisory Group</small></div>
</section>

<section class="sheet envelope-back">
  <div class="body"></div>
  <svg viewBox="0 0 386 60" width="386" height="60">
    <path d="M0 0H386L380 50Q378 58 368 58H18Q8 58 6 50Z" fill="var(--green)"/>
  </svg>
  <div class="brand">Clearpath</div>
</section>

<section class="sheet envelope-front">
  <div class="brand">Clearpath<small>Advisory Group</small></div>
  <div class="address">4200 Linden Ave Suite 210,<br>Springfield USA 62704</div>
  <svg class="wave" viewBox="0 0 386 30" width="386" height="30" preserveAspectRatio="none">
    <path d="M30 30 Q170 3 280 2 L240 4 Q150 10 60 30Z" fill="var(--yellow)"/>
    <path d="M55 30 Q200 6 386 7 L386 30Z" fill="var(--green)"/>
  </svg>
</section>

</body>
</html>
```